Storm Restoration Contractor needs a professional business card design

Looking for a professional business card design. Not looking for your cheapo MS Word standard ones that are readily available. Dont want it to be cookie cutter look like ones readily available online. We just recently changed our logo and want to freshen up all our documents. Our company handles restoring a property back to a pre-loss condition after a storm damages it. For example, wind, hail, flood, fire losses.

Target Market(s)

Property Owners, Homeowners, Property Owners, Commercial Property Owners, Property Management Companies, Hail and Wind Damaged Properties

Industry/Entity Type

Construction Company

Contact Information for Business Card

Brightline Facades
847-555-0193
847-555-0147 fax
www.brightlinefacades.example
info@brightlinefacades.example

Requirements
Must have
• Clean, Professional, fresh look
• Storm Restoration, Roofing, Siding, Windows
Nice to have
• If there is a way to incorporate storms that may be cool.

```html
<!DOCTYPE html>
<html lang="en">
<head>
<meta charset="utf-8">
<title>Brightline Facades – Business Card</title>
<link href="https://fonts.googleapis.com/css2?family=Open+Sans:wght@400;600;700&display=swap" rel="stylesheet">
<style>
  :root {
    --bg: #2a2a2a;
    --brand-blue: #1f74bb;
    --brand-blue-soft: #2a7fc4;
    --slate: #58595b;
    --white: #ffffff;
    --ink-light: #e8eef5;
  }
  * { box-sizing: border-box; margin: 0; padding: 0; }
  html, body { width: 1200px; height: 907px; overflow: hidden; }
  body {
    background: var(--bg);
    font-family: "Open Sans", Arial, sans-serif;
    position: relative;
  }
  .card {
    position: absolute;
    left: 300px;
    width: 600px;
    height: 343px;
    overflow: hidden;
    box-shadow: 0 10px 30px rgba(0,0,0,0.45);
  }
  .card--front { top: 62px; background: var(--white); }
  .card--back { top: 483px; background: var(--slate); }

  .front__panel {
    position: absolute; left: 0; top: 0;
    width: 310px; height: 100%;
    background: var(--brand-blue);
  }
  .front__panel-circle {
    position: absolute; left: 266px; top: 128px;
    width: 88px; height: 88px; border-radius: 50%;
    background: var(--brand-blue);
  }
  .front__ghost-circle {
    position: absolute; left: 40px; top: -30px;
    width: 230px; height: 230px; border-radius: 50%;
    border: 26px solid var(--brand-blue-soft);
  }
  .brand-mark {
    position: absolute; left: 280px; top: 142px;
    width: 60px; height: 60px; border-radius: 50%;
    background: var(--white);
    border: 5px solid var(--brand-blue);
  }
  .brand-name {
    position: absolute; left: 366px; top: 130px;
    color: var(--brand-blue);
    font-weight: 700; font-size: 28px; line-height: 1.05;
    letter-spacing: 1px; text-transform: uppercase;
  }

  .contact {
    position: absolute; left: 30px; top: 186px;
    color: var(--white);
  }
  .contact__name { font-weight: 700; font-size: 19px; }
  .contact__role { font-size: 13px; margin: 2px 0 12px 22px; }
  .contact__list { list-style: none; margin-left: 22px; }
  .contact__item {
    display: flex; align-items: center; gap: 7px;
    font-size: 13px; line-height: 19px; color: var(--ink-light);
  }
  .contact__item svg { width: 13px; height: 13px; flex: none; }

  .back__mark {
    position: absolute; left: 250px; top: 60px;
    width: 100px; height: 100px; border-radius: 50%;
    background: var(--white);
    border: 7px solid var(--brand-blue);
  }
  .back__name {
    position: absolute; left: 0; right: 0; top: 178px;
    text-align: center; color: var(--white);
    font-weight: 700; font-size: 22px; letter-spacing: 1px;
    text-transform: uppercase;
  }
  .back__services {
    position: absolute; left: 0; right: 0; top: 248px;
    text-align: center; color: var(--white);
    font-size: 14px; letter-spacing: 0.5px;
  }
  .back__web {
    position: absolute; left: 0; right: 0; top: 270px;
    text-align: center; color: var(--white); font-size: 13px;
  }
</style>
</head>
<body>

<section class="card card--front">
  <div class="front__panel">
    <div class="front__ghost-circle"></div>
  </div>
  <div class="front__panel-circle"></div>
  <div class="brand-mark"></div>
  <div class="brand-name">Brightline<br>Facades</div>

  <div class="contact">
    <div class="contact__name">Daniel Marsh</div>
    <div class="contact__role">Director</div>
    <ul class="contact__list">
      <li class="contact__item">
        <svg viewBox="0 0 16 16"><path fill="#fff" d="M3 1h3l1 4-2 1c1 2 3 4 5 5l1-2 4 1v3c0 1-1 2-2 2C7 15 1 9 1 3c0-1 1-2 2-2z"/></svg>
        847-555-0193
      </li>
      <li class="contact__item">
        <svg viewBox="0 0 16 16"><rect x="4" y="1" width="8" height="4" fill="#fff"/><rect x="1" y="5" width="14" height="7" rx="1" fill="#fff"/><rect x="4" y="10" width="8" height="5" fill="#fff" stroke="#1f74bb"/></svg>
        847-555-0147
      </li>
      <li class="contact__item">
        <svg viewBox="0 0 16 16"><rect x="1" y="3" width="14" height="10" rx="1" fill="#fff"/><path d="M1 4l7 5 7-5" fill="none" stroke="#1f74bb" stroke-width="1.3"/></svg>
        info@brightlinefacades.example
      </li>
      <li class="contact__item">
        <svg viewBox="0 0 16 16" fill="none" stroke="#fff" stroke-width="1.3"><circle cx="8" cy="8" r="6.5"/><ellipse cx="8" cy="8" rx="3" ry="6.5"/><path d="M1.5 8h13M2.5 5h11M2.5 11h11"/></svg>
        www.brightlinefacades.example
      </li>
    </ul>
  </div>
</section>

<section class="card card--back">
  <div class="back__mark"></div>
  <div class="back__name">Brightline Facades</div>
  <div class="back__services">STORM RESTORATION | ROOFING | SIDING | WINDOWS</div>
  <div class="back__web">www.brightlinefacades.example</div>
</section>

</body>
</html>
```